Web Design Project

To develop a web based Council Meeting Support system which includes 2 major components for each Council member:
1. Allow a council member to Vote on a motion during a council session
2. Allow a council member to flag notify the Chair their intention to speak on a motion
The application will have 3 separate interfaces:
Chair interface: Allows the Chair of the session to review voting and manage the speaker queue
Council interface: Allows each council member to vote on each motion and add flag their intention to speak for or against a motion
Admin interface: Allows administrators to initiate a session and import details on all meeting participants
We will begin by designing the Council Interface. (An example wireframe is attached) This council interface will give members the ability to request to speak, vote, view voting results and viewing the current motion number.
*** 4 Designs will be required overall. One for each interface and a login page ***
Needs to be designed so that it works well on an Velbo or any tablet device.
Update: Looking for a brighter design, not a dark grey one. The blue colour from trm.on.ca would be good.
Flag
- Request to Speak
Voting
Vote Results
Current Motion Number

```html
<!DOCTYPE html>
<html lang="en">
<head>
<meta charset="utf-8">
<title>Council Interface</title>
<link rel="stylesheet" href="https://fonts.googleapis.com/css2?family=PT+Sans+Narrow&family=PT+Sans&display=swap">
<style>
:root{
  --navy:#063566;
  --navy-top:#0f4c8a;
  --navy-bottom:#032c57;
  --ink:#0b3a6e;
  --rule:#b9c3cf;
  --panel-line:#a9adb2;
  --results-bg:#deedfb;
  --results-line:#c4d8ec;
  --white:#ffffff;
}
*{box-sizing:border-box;margin:0;padding:0}
html,body{width:1200px;height:785px;overflow:hidden;background:var(--white)}
body{position:relative;font-family:"PT Sans",sans-serif;color:var(--ink)}
.edge{position:absolute;left:0;width:1200px;height:2px;background:var(--navy)}
.edge--top{top:0}
.edge--bottom{top:782px}

.brand{position:absolute;left:166px;top:12px;display:flex;align-items:center;gap:8px}
.brand__mark{width:26px;height:26px;background:var(--navy)}
.brand__name{font-family:"PT Sans",sans-serif;font-weight:700;font-size:13px;line-height:14px;color:var(--navy);width:130px}

.motion{position:absolute;left:861px;top:18px;width:178px;height:32px;border:1px solid var(--panel-line);display:flex}
.motion__label{background:var(--navy);color:var(--white);font-family:"PT Sans Narrow",sans-serif;font-size:15px;width:95px;display:flex;align-items:center;justify-content:center;margin:1px}

.panel{position:absolute;left:165px;width:873px;border:1px solid var(--panel-line);background:var(--white)}
.panel--speak{top:60px;height:261px}
.panel--vote{top:330px;height:403px}

.speak__title{position:absolute;left:111px;top:17px;font-family:"PT Sans Narrow",sans-serif;font-size:22px;color:var(--ink)}
.speak__rule{position:absolute;left:111px;top:44px;width:642px;height:1px;background:var(--rule)}
.speak__edge{position:absolute;left:752px;top:51px;width:1px;height:122px;background:var(--rule)}

.btn{position:absolute;display:flex;align-items:center;justify-content:center;color:var(--white);
  font-family:"PT Sans Narrow",sans-serif;font-size:22px;letter-spacing:.2px;
  background:linear-gradient(var(--navy-top),var(--navy-bottom));
  border:2px solid var(--white);box-shadow:1px 2px 4px rgba(0,0,0,.45)}
.btn--for-motion{left:110px;top:66px;width:213px;height:54px}
.btn--against-motion{left:326px;top:123px;width:213px;height:54px}
.btn--remove{left:542px;top:179px;width:215px;height:55px}

.vote__title{position:absolute;left:17px;top:20px;font-family:"PT Sans Narrow",sans-serif;font-size:22px}
.btn--for{left:20px;top:56px;width:214px;height:54px}
.btn--against{left:20px;top:122px;width:214px;height:54px}
.btn--abstain{left:20px;top:193px;width:214px;height:54px}

.results{position:absolute;left:264px;top:17px;width:593px;height:372px;background:var(--results-bg);border:1px solid var(--results-line)}
.results__title{position:absolute;left:0;right:0;top:13px;text-align:center;font-family:"PT Sans Narrow",sans-serif;font-size:22px}
.tally{position:absolute;top:52px;width:180px;height:310px;background:var(--white)}
.tally--for{left:10px}
.tally--against{left:203px}
.tally--abstain{left:397px}
.tally__head{font-family:"PT Sans Narrow",sans-serif;font-size:20px;padding:8px 0 3px 11px;margin:0 1px;border-bottom:1px solid #d8e1ea}
.tally__list{list-style:none;padding:8px 0 0 15px}
.tally__list li{font-size:11.5px;line-height:22.2px}

.footer{position:absolute;left:0;width:1200px;top:751px;text-align:center;font-size:11px;color:var(--ink)}
</style>
</head>
<body>
<div class="edge edge--top"></div>

<header>
  <div class="brand"><span class="brand__mark"></span><span class="brand__name">Northfield Engineers Guild</span></div>
  <div class="motion"><span class="motion__label">Current Motion</span></div>
</header>

<section class="panel panel--speak">
  <h2 class="speak__title">I would like to speake</h2>
  <div class="speak__rule"></div>
  <div class="speak__edge"></div>
  <div class="btn btn--for-motion">FOR MOTION</div>
  <div class="btn btn--against-motion">AGAINST MOTION</div>
  <div class="btn btn--remove">REMOVE FROM QUEUE</div>
</section>

<section class="panel panel--vote">
  <h2 class="vote__title">Voting</h2>
  <div class="btn btn--for">FOR</div>
  <div class="btn btn--against">AGAINST</div>
  <div class="btn btn--abstain">ABSTAIN</div>

  <div class="results">
    <h3 class="results__title">Vote Results</h3>
    <div class="tally tally--for">
      <h4 class="tally__head">For</h4>
      <ul class="tally__list">
        <li>A. Marchand</li><li>S.Vellor</li><li>I. Dorsa</li><li>T.Lanning</li><li>R.A. Pellow</li>
        <li>S.K. Narvel</li><li>S.Vellor</li><li>L.Rowe</li><li>B.Halvik</li>
      </ul>
    </div>
    <div class="tally tally--against">
      <h4 class="tally__head">Against</h4>
      <ul class="tally__list">
        <li>J.D. Corwin</li><li>S.Ostrin</li><li>D.Melvas</li><li>D.Tarno</li><li>B.Kelm</li><li>R.J. Brisco</li>
        <li>R.Feldt</li><li>W.Ambry</li><li>M.Hale Corbin</li><li>S.Quill</li><li>C.D. Vance</li><li>T.Orlan</li>
      </ul>
    </div>
    <div class="tally tally--abstain">
      <h4 class="tally__head">Abstain</h4>
      <ul class="tally__list">
        <li>R.K. Dervanath</li><li>M.Pruell</li><li>C.Bream</li><li>M.Tolo</li><li>R.Garnet</li>
      </ul>
    </div>
  </div>
</section>

<footer class="footer">Copyrights @ 2012 All Rights Reserved</footer>
<div class="edge edge--bottom"></div>
</body>
</html>
```